Folded A4 flyer for design&construction company

Folded A4 flyer needed. Keywords: elegant, stylish
our website www.dravimo.ae

Industry/Entity Type

Construction

```html
<!DOCTYPE html>
<html lang="en">
<head>
<meta charset="utf-8">
<title>Dravimo – Services Flyer</title>
<link rel="stylesheet" href="https://fonts.googleapis.com/css2?family=Roboto+Condensed:wght@400;500&display=swap">
<style>
  :root {
    --teal: #137b7c;
    --orange: #f39322;
    --ink: #1c1c1c;
    --text: #2a2a2a;
    --paper: #ffffff;
    --rule: #d6d6d6;
    --footer: #2b2b2d;
  }
  * { margin: 0; padding: 0; box-sizing: border-box; }
  html, body { width: 1200px; height: 848px; overflow: hidden; background: var(--paper); }
  body { font-family: "Roboto Condensed", "Arial Narrow", sans-serif; color: var(--text); position: relative; }

  .service-card {
    position: absolute;
    width: 508px;
    height: 346px;
    border-bottom: 1px solid var(--rule);
    overflow: hidden;
    background: var(--paper);
  }
  .card-design      { left: 46px;  top: 50px; }
  .card-fitout      { left: 646px; top: 50px; }
  .card-landscaping { left: 46px;  top: 442px; }
  .card-maintenance { left: 646px; top: 442px; }

  .card-photo { position: absolute; inset: 0; }
  .card-design .card-photo {
    background: linear-gradient(90deg, #ffffff 0%, rgba(255,255,255,0.85) 22%, rgba(255,255,255,0) 48%),
                radial-gradient(circle at 58% 25%, #e8c27a 0%, #a86f2c 25%, #5d3a18 60%, #2e1a0b 100%);
  }
  .card-fitout .card-photo {
    background: linear-gradient(90deg, #ffffff 0%, rgba(255,255,255,0.9) 22%, rgba(255,255,255,0) 52%),
                linear-gradient(180deg, #111 0%, #3a3a3a 30%, #bdbdbd 52%, #6c6c6c 72%, #1e1e1e 100%);
  }
  .card-landscaping .card-photo {
    background: linear-gradient(90deg, #ffffff 0%, rgba(255,255,255,0.8) 25%, rgba(255,255,255,0) 50%),
                linear-gradient(180deg, #1d3a4d 0%, #2d5a68 30%, #c29a4a 52%, #1f4a4a 70%, #0f2a2c 100%);
  }
  .card-maintenance .card-photo {
    background: linear-gradient(90deg, #ffffff 0%, rgba(255,255,255,0.9) 25%, rgba(255,255,255,0) 52%),
                repeating-linear-gradient(168deg, #cfcfcf 0 38px, #a9a9a9 38px 52px, #e2e2e2 52px 66px);
  }

  .card-label {
    position: absolute;
    left: 0; top: 0;
    height: 32px;
    padding-left: 17px;
    color: #fff;
    background: var(--teal);
    font-size: 20px;
    line-height: 32px;
    font-weight: 400;
    letter-spacing: 0.2px;
    clip-path: polygon(0 0, 100% 0, calc(100% - 13px) 100%, 0 100%);
  }
  .card-label::after { content: none; }
  .label-accent {
    position: absolute;
    top: 0;
    width: 28px;
    height: 32px;
    background: var(--orange);
    clip-path: polygon(16px 0, 28px 0, 12px 100%, 0 100%);
  }
  .card-design .card-label, .card-fitout .card-label { width: 158px; }
  .card-design .label-accent, .card-fitout .label-accent { left: 148px; }
  .card-landscaping .card-label, .card-maintenance .card-label { width: 166px; }
  .card-landscaping .label-accent, .card-maintenance .label-accent { left: 156px; }

  .brand-name {
    position: absolute;
    left: 12px;
    top: 78px;
    font-size: 27px;
    font-weight: 400;
    letter-spacing: 0.5px;
    color: var(--ink);
    line-height: 1;
  }

  .service-list {
    position: absolute;
    left: 12px;
    top: 130px;
    list-style: none;
    font-size: 14px;
    line-height: 24.2px;
    color: var(--text);
  }
  .card-maintenance .service-list { left: 14px; }
  .service-list .note { display: block; font-size: 9.5px; line-height: 10px; }

  .footer-band {
    position: absolute;
    left: 0; top: 832px;
    width: 1200px; height: 16px;
    background: var(--footer);
  }
</style>
</head>
<body>

  <section class="service-card card-design">
    <div class="card-photo" role="img" aria-label="Photo of an ornate classical interior with a crystal chandelier and antique furniture"></div>
    <h2 class="card-label">DESIGN</h2><span class="label-accent"></span>
    <div class="brand-name">DRAVIMO</div>
    <ul class="service-list">
      <li>Villas Interior Design</li>
      <li>Villas Exterior Design</li>
      <li>Landscape Design</li>
      <li>Retail Interior Design</li>
      <li>Office Interior Design</li>
      <li>Hospitality Interior Design</li>
      <li>Hotel Interior Design</li>
      <li>Hotel Exterior Design</li>
      <li>Restaurant Interior Design</li>
    </ul>
  </section>

  <section class="service-card card-fitout">
    <div class="card-photo" role="img" aria-label="Black and white photo of people silhouetted against a glass wall overlooking a city"></div>
    <h2 class="card-label">FITOUT</h2><span class="label-accent"></span>
    <div class="brand-name">DRAVIMO</div>
    <ul class="service-list">
      <li>Development Approvals</li>
      <li>Flooring Solutions</li>
      <li>Partition</li>
      <li>Sealing Solutions</li>
      <li>MEP Works</li>
      <li>Civil Works</li>
      <li>Joinery</li>
      <li>Glass and Aluminium Works<span class="note">(subcontractor)</span></li>
    </ul>
  </section>

  <section class="service-card card-landscaping">
    <div class="card-photo" role="img" aria-label="Night photo of a waterfront city skyline with lights reflected on the water"></div>
    <h2 class="card-label">LANDSCAPING</h2><span class="label-accent"></span>
    <div class="brand-name">DRAVIMO</div>
    <ul class="service-list">
      <li>Soft Landscaping</li>
      <li>Irrigation Solutions</li>
      <li>Hard land Scaping</li>
      <li>External Lighting</li>
      <li>Swimming Pool &amp; Water Features</li>
    </ul>
  </section>

  <section class="service-card card-maintenance">
    <div class="card-photo" role="img" aria-label="Photo of a concrete building under construction with shoring props between floors"></div>
    <h2 class="card-label">MAINTENANCE</h2><span class="label-accent"></span>
    <div class="brand-name">DRAVIMO</div>
    <ul class="service-list">
      <li>AC Repair</li>
      <li>Plumber Services</li>
      <li>Electric Repair</li>
      <li>Carpentry Work</li>
      <li>Gypsum Ceiling</li>
      <li>Painting Services</li>
      <li>Cleaning Services</li>
      <li>Emergency Services</li>
    </ul>
  </section>

  <div class="footer-band"></div>

</body>
</html>
```